Our architectural studio needs a new business card

We need a business card design for our studio based in Valmoreau in Belgium. We are active in architecture, design and installation.
Our works are contemporary and minimalist. our clients are refined and cultured.
Our business card must be minimalist and refined.

Reason: Some designers have accepted my invitation but they don't have all replied. I want to give them a chance to make one proposal. Paul

Target Market(s)

architecture

Industry/Entity Type

Business

Contact Information for Business Card

studio: paul dorsande studio
paul dorsande, architecte
M. +32 471 982 615
F. +322 618 4097
www.pauldorsande-example.com
paul@pauldorsande-example.com
14 rue des Margelles
1490 Valmoreau
Belgium

Font styles to use
Sans Serif

Requirements
Must have
• simple, minimalist, clear, elegant and chic! Black and white
Nice to have
• embossed logo, other format like a square for example
Should not have
• color, fantasy, curves, ...

```html
<!DOCTYPE html>
<html lang="fr">
<head>
<meta charset="utf-8">
<title>paul dorsande studio — business card</title>
<link rel="stylesheet" href="https://fonts.googleapis.com/css2?family=Arimo:wght@400&family=Montserrat:wght@500&display=swap">
<style>
  :root {
    --backdrop: #e6e6e4;
    --paper: #ffffff;
    --ink: #3a3637;
    --ink-soft: #4a4647;
    --rule: #5a5657;
  }
  * { margin: 0; padding: 0; box-sizing: border-box; }
  html, body { width: 1200px; height: 1000px; overflow: hidden; }
  body {
    background: var(--backdrop);
    position: relative;
    font-family: "Arimo", Arial, sans-serif;
    color: var(--ink);
  }
  .card {
    position: absolute;
    width: 600px;
    height: 380px;
    background: var(--paper);
    box-shadow: 0 2px 6px rgba(0,0,0,0.12);
  }
  .card--contact { left: 110px; top: 90px; }
  .card--studio  { left: 490px; top: 530px; }

  /* shared studio mark: plain square + name in the text font */
  .studio-mark {
    position: absolute;
    display: flex;
    align-items: flex-end;
    gap: 8px;
    white-space: nowrap;
  }
  .studio-mark__square { width: 38px; height: 38px; background: var(--ink); flex: none; }
  .studio-mark__name { font-size: 11px; line-height: 1; color: var(--ink); }

  /* contact side */
  .card--contact .studio-mark { left: 250px; top: 56px; }
  .divider {
    position: absolute;
    left: 290px;
    top: 102px;
    width: 1px;
    height: 228px;
    background: var(--rule);
  }
  .person {
    position: absolute;
    right: 318px;
    top: 184px;
    text-align: right;
    white-space: nowrap;
  }
  .person__name { font-size: 15px; color: var(--ink-soft); line-height: 1.2; }
  .person__role { font-size: 10px; color: var(--ink-soft); line-height: 1.3; }
  .contact-list {
    position: absolute;
    left: 300px;
    top: 226px;
    list-style: none;
    font-size: 12px;
    line-height: 15px;
    color: var(--ink-soft);
    white-space: nowrap;
  }

  /* studio side */
  .card--studio .studio-mark {
    left: 0; right: 0; top: 118px;
    justify-content: center;
  }
  .card--studio .studio-mark__square { width: 56px; height: 56px; }
  .card--studio .studio-mark__name { font-size: 14px; }
  .studio-caption {
    position: absolute;
    left: 0; right: 0; top: 236px;
    text-align: center;
    font-family: "Montserrat", Arial, sans-serif;
    font-weight: 500;
    font-size: 10px;
    letter-spacing: 3px;
    text-transform: uppercase;
    color: var(--ink);
  }
</style>
</head>
<body>
  <section class="card card--contact" aria-label="Contact side">
    <div class="studio-mark">
      <span class="studio-mark__square"></span>
      <span class="studio-mark__name">paul dorsande studio</span>
    </div>
    <div class="divider"></div>
    <div class="person">
      <p class="person__name">Paul Dorsande</p>
      <p class="person__role">architecte</p>
    </div>
    <ul class="contact-list">
      <li>M. +32 471 982 615</li>
      <li>F. +322 618 4097</li>
      <li>www.pauldorsande-example.com</li>
      <li>paul@pauldorsande-example.com</li>
      <li>14 rue des Margelles 1490</li>
      <li>Valmoreau Belgium</li>
    </ul>
  </section>

  <section class="card card--studio" aria-label="Studio side">
    <div class="studio-mark">
      <span class="studio-mark__square"></span>
      <span class="studio-mark__name">paul dorsande</span>
    </div>
    <p class="studio-caption">Paul Dorsande Studio</p>
  </section>
</body>
</html>
```